Criação de Papelaria Profissional para Advocacia e Direito
A empresa queria:
" Somos um escritório de advocacia full-service, com sede em Santarém-PA e uma unidade em Manaus-AM. Temos atuação em todo o Brasil. "

```html
<!DOCTYPE html>
<html lang="pt-BR">
<head>
<meta charset="utf-8">
<title>Assinatura de e-mail — Henrique Valadares Advocacia</title>
<link rel="stylesheet" href="https://fonts.googleapis.com/css2?family=Cinzel:wght@400;500&family=Montserrat:wght@400;500;600&display=swap">
<style>
  :root {
    --page: #ffffff;
    --navy: #15304a;
    --sand: #ecebde;
    --gold: #c9a37b;
    --copper: #c48c63;
    --ink: #2c3440;
    --ink-soft: #4f5864;
    --rule: #c9c5b3;
    --light: #e9e3d6;
  }
  * { margin: 0; padding: 0; box-sizing: border-box; }
  html, body { width: 1200px; height: 1200px; overflow: hidden; background: var(--page); }
  body { position: relative; font-family: "Montserrat", sans-serif; color: var(--ink); }

  .signature {
    position: absolute;
    left: 60px; top: 440px;
    width: 1080px; height: 276px;
    display: flex;
  }

  .brand-panel {
    position: relative;
    width: 440px; height: 100%;
    background: var(--navy);
    clip-path: polygon(0 0, 100% 0, 100% 74%, 93% 100%, 0 100%);
    display: flex; flex-direction: column; align-items: center; justify-content: center;
    gap: 14px;
  }
  .brand-mark {
    width: 44px; height: 44px;
    border: 2px solid var(--light);
  }
  .brand-name {
    font-family: "Cinzel", serif;
    font-weight: 400;
    font-size: 30px;
    letter-spacing: 1px;
    color: var(--light);
  }
  .brand-tagline {
    font-size: 9px;
    letter-spacing: 2px;
    color: var(--light);
    opacity: .8;
    margin-top: -8px;
  }

  .info-panel {
    position: relative;
    flex: 1;
    margin-left: -30px;
    background: var(--sand);
    padding: 42px 36px 0 60px;
  }
  .info-top { display: flex; justify-content: space-between; }
  .person-name {
    font-family: "Cinzel", serif;
    font-size: 25px;
    color: var(--gold);
    letter-spacing: .5px;
  }
  .person-role, .person-id { font-size: 14px; color: var(--ink-soft); line-height: 1.5; }
  .person-role { margin-top: 8px; }

  .contacts { list-style: none; width: 290px; }
  .contacts li { display: flex; align-items: center; gap: 8px; font-size: 13.5px; color: var(--ink-soft); line-height: 28px; }
  .contacts svg { width: 14px; height: 14px; fill: var(--ink-soft); flex: none; }
  .contacts .website { font-weight: 600; color: var(--ink); }

  .divider { height: 1px; background: var(--rule); margin: 14px 0 16px; }

  .units { display: flex; justify-content: space-between; }
  .unit { display: flex; align-items: center; gap: 10px; width: 290px; }
  .unit svg { width: 14px; height: 18px; fill: var(--ink-soft); flex: none; }
  .unit-title { font-size: 13.5px; font-weight: 600; color: var(--ink); }
  .unit-address { font-size: 12.5px; color: var(--ink-soft); line-height: 1.45; }

  .social {
    position: absolute;
    right: 40px; top: 360px;
    display: flex; gap: 14px; list-style: none;
  }
  .social li { width: 28px; height: 28px; border-radius: 50%; background: var(--copper); }
</style>
</head>
<body>
  <section class="signature" aria-label="Assinatura de e-mail">
    <div class="brand-panel">
      <div class="brand-mark"></div>
      <div class="brand-name">HENRIQUE VALADARES</div>
      <div class="brand-tagline">ADVOCACIA E CONSULTORIA</div>
    </div>

    <div class="info-panel">
      <div class="info-top">
        <div class="person">
          <div class="person-name">HENRIQUE VALADARES</div>
          <div class="person-role">Fundador e Sócio Sênior</div>
          <div class="person-id">OAB/PA 00.000</div>
        </div>
        <ul class="contacts">
          <li>
            <svg viewBox="0 0 24 24"><path d="M6.6 10.8a15.1 15.1 0 0 0 6.6 6.6l2.2-2.2a1 1 0 0 1 1-.25 11.4 11.4 0 0 0 3.6.57 1 1 0 0 1 1 1V20a1 1 0 0 1-1 1A17 17 0 0 1 3 4a1 1 0 0 1 1-1h3.5a1 1 0 0 1 1 1c0 1.25.2 2.45.57 3.57a1 1 0 0 1-.25 1z"/></svg>
            (93) 99000-1234
          </li>
          <li>
            <svg viewBox="0 0 24 24"><path d="M3 5h18v14H3zm2 2v.5l7 4.5 7-4.5V7zm0 2.8V17h14V9.8l-7 4.5z"/></svg>
            escritorio@valadaresadv.com.br
          </li>
          <li class="website">valadaresadv.com.br</li>
        </ul>
      </div>

      <div class="divider"></div>

      <div class="units">
        <div class="unit">
          <svg viewBox="0 0 14 18"><path d="M7 0a7 7 0 0 0-7 7c0 5 7 11 7 11s7-6 7-11a7 7 0 0 0-7-7zm0 9.5A2.5 2.5 0 1 1 7 4.5a2.5 2.5 0 0 1 0 5z"/></svg>
          <div>
            <div class="unit-title">Unidade Matriz</div>
            <div class="unit-address">Av. das Palmeiras, nº 1200 -<br>Jardim Central - Santarém - PA.</div>
          </div>
        </div>
        <div class="unit">
          <svg viewBox="0 0 14 18"><path d="M7 0a7 7 0 0 0-7 7c0 5 7 11 7 11s7-6 7-11a7 7 0 0 0-7-7zm0 9.5A2.5 2.5 0 1 1 7 4.5a2.5 2.5 0 0 1 0 5z"/></svg>
          <div>
            <div class="unit-title">Unidade Manaus</div>
            <div class="unit-address">Rua das Acácias, nº 450 -<br>Bela Vista - Manaus - AM.</div>
          </div>
        </div>
      </div>
    </div>

    <ul class="social" aria-label="Redes sociais">
      <li></li><li></li><li></li><li></li><li></li>
    </ul>
  </section>
</body>
</html>
```